LEARN Business Skills so you can Earn a good living

size of the poster is 8”x 10.75" plus 0.25" bleed.
Please leave 1 inch on the bottoum for footer
I want a design a poster that will attract people's attention.
I appreciate a creative ad however the ad should not take away from being able to clearly read the text.
-I also appreciate a simple creative ad that is not too busy.
-you can use graphics, vectors, or pictures of real people.
-however, if you use real people it should be a white male that is wearing a white shirt and look like a professional person.

Target Market(s)

Potential young business people

Industry/Entity Type

education

Requirements
Must have
• easy to read the text
Nice to have
• I would like a "creative" simple ad that is easy to be read
Should not have
• pictures of women

```html
<!DOCTYPE html>
<html lang="en">
<head>
<meta charset="utf-8">
<title>Learn to Earn – Business Enrichment Course</title>
<link rel="stylesheet" href="https://fonts.googleapis.com/css2?family=Jost:wght@500;600;700&family=Poppins:wght@400;500;600;700&display=swap">
<style>
  :root {
    --yellow: #FFDE00;
    --navy: #1F2D3E;
    --red: #E31B1B;
    --white: #FFFFFF;
    --ink: #0B0B0B;
    --chart: #2E6E96;
    --divider: #D9D9D9;
  }
  * { margin: 0; padding: 0; box-sizing: border-box; }
  html, body { width: 862px; height: 1200px; overflow: hidden; background: var(--white); }
  .poster { position: relative; width: 862px; height: 1200px; overflow: hidden; background: var(--white); font-family: "Poppins", sans-serif; }

  .backdrop { position: absolute; inset: 0; }

  .megaphone-art { position: absolute; left: 0; top: 132px; width: 200px; height: 250px;
    background: linear-gradient(135deg, #f2f2f2 0%, #c9c9c9 55%, #b52020 100%); border-radius: 40px 120px 120px 40px; opacity: .92; }
  .presenter-art { position: absolute; left: 700px; top: 58px; width: 150px; height: 745px;
    background: linear-gradient(180deg, #c58b56 0%, #d9a878 18%, #ffffff 26%, #ffffff 46%, #8a867d 54%, #7d796f 94%, #4a2d22 100%);
    border-radius: 70px 70px 24px 24px; }

  .headline { position: absolute; font-family: "Jost", sans-serif; font-weight: 700; line-height: 1; }
  .headline--learn { left: 290px; top: 16px; font-size: 128px; color: var(--ink); letter-spacing: -3px; }
  .headline--to { left: 390px; top: 126px; font-size: 128px; color: var(--ink); letter-spacing: -3px; }
  .earn-box { position: absolute; left: 290px; top: 254px; width: 312px; height: 111px; background: var(--white); }
  .headline--earn { left: 303px; top: 240px; font-size: 128px; color: var(--red); letter-spacing: -3px; }

  .course-title { position: absolute; left: 84px; top: 456px; font-family: "Jost", sans-serif; font-weight: 600; font-size: 91px; line-height: 85px; letter-spacing: -1px; }
  .course-title span { display: block; }
  .course-title .line-white { color: var(--white); }
  .course-title .line-yellow { color: var(--yellow); }

  .tagline { position: absolute; left: 86px; top: 728px; width: 640px; font-family: "Jost", sans-serif; font-weight: 600; font-size: 24px; line-height: 29px; color: var(--white); letter-spacing: -.2px; }
  .tagline em { font-style: normal; color: var(--yellow); }

  .benefits { position: absolute; left: 31px; top: 808px; width: 798px; height: 108px; background: var(--white); border-radius: 12px; display: flex; align-items: center; box-shadow: 0 14px 14px -8px rgba(0,0,0,.35); }
  .benefits__label { width: 244px; height: 108px; background: var(--red); border-radius: 12px; color: var(--white); font-family: "Jost", sans-serif; font-weight: 600; font-size: 25px; line-height: 28px; padding: 10px 0 0 31px; letter-spacing: -.3px; }
  .benefit { display: flex; align-items: center; gap: 12px; height: 82px; padding-left: 18px; font-size: 17px; line-height: 21px; color: #1a1a1a; }
  .benefit svg { flex: none; }
  .benefit--job { width: 174px; }
  .benefit--business { width: 200px; border-left: 1px solid var(--divider); }
  .benefit--salary { width: 180px; border-left: 1px solid var(--divider); }

  .topics { position: absolute; top: 943px; left: 0; width: 862px; height: 148px; }
  .topics__col { position: absolute; top: 0; list-style: none; font-size: 12.2px; font-weight: 600; color: #1f1f1f; line-height: 19.6px; }
  .topics__col li { position: relative; padding-left: 18px; white-space: nowrap; }
  .topics__col li::before { content: ""; position: absolute; left: 0; top: 6px; width: 7px; height: 7px; border-radius: 50%; background: var(--navy); }
  .topics__col--a { left: 51px; }
  .topics__col--b { left: 324px; }
  .topics__col--c { left: 688px; }
  .topics__rule { position: absolute; top: 8px; width: 1px; height: 130px; background: rgba(0,0,0,.12); }
  .topics__rule--first { left: 295px; }
  .topics__rule--second { left: 650px; }
</style>
</head>
<body>
<div class="poster">

  <svg class="backdrop" width="862" height="1200" viewBox="0 0 862 1200" aria-hidden="true">
    <path d="M0 415 Q90 330 195 292 L862 292 L862 877 L0 877 Z" fill="var(--navy)"/>
    <rect x="0" y="877" width="862" height="214" fill="var(--yellow)"/>
    <ellipse cx="451" cy="92" rx="330" ry="348" fill="var(--yellow)"/>
    <path d="M195 292 L165 368 L245 350 Z" fill="var(--yellow)"/>
    <g class="growth-chart" fill="var(--chart)" opacity=".55">
      <rect x="420" y="690" width="10" height="28"/>
      <rect x="438" y="672" width="10" height="46"/>
      <rect x="456" y="684" width="10" height="34"/>
      <rect x="474" y="660" width="10" height="58"/>
      <rect x="492" y="676" width="10" height="42"/>
      <rect x="510" y="650" width="10" height="68"/>
      <rect x="528" y="668" width="10" height="50"/>
      <rect x="546" y="640" width="10" height="78"/>
      <rect x="564" y="654" width="10" height="64"/>
      <rect x="582" y="628" width="10" height="90"/>
      <rect x="600" y="644" width="10" height="74"/>
      <rect x="618" y="612" width="10" height="106"/>
      <rect x="636" y="624" width="10" height="94"/>
      <rect x="654" y="600" width="10" height="118"/>
      <rect x="672" y="610" width="10" height="108"/>
      <rect x="690" y="584" width="10" height="134"/>
      <rect x="708" y="594" width="10" height="124"/>
      <rect x="726" y="570" width="10" height="148"/>
      <rect x="744" y="580" width="10" height="138"/>
      <rect x="762" y="556" width="10" height="162"/>
      <rect x="780" y="546" width="10" height="172"/>
      <rect x="798" y="532" width="10" height="186"/>
      <rect x="816" y="520" width="10" height="198"/>
    </g>
    <path d="M420 715 Q600 710 720 610" fill="none" stroke="#c9b9a3" stroke-width="2" opacity=".7"/>
    <polyline points="420,630 470,590 500,612 540,560 575,585 610,545 650,570 690,530 730,555 770,520" fill="none" stroke="#7fd0c8" stroke-width="1.5" stroke-dasharray="3 3" opacity=".6"/>
  </svg>

  <div class="megaphone-art" role="img" aria-label="Illustration of a white and red megaphone with sound bolts"></div>
  <div class="presenter-art" role="img" aria-label="Illustration of a bearded businessman in a white shirt and grey trousers giving a thumbs up"></div>

  <div class="headline headline--learn">LEARN</div>
  <div class="headline headline--to">TO</div>
  <div class="earn-box"></div>
  <div class="headline headline--earn">EARN</div>

  <h1 class="course-title">
    <span class="line-white">BUSINESS</span>
    <span class="line-yellow">ENRICHMENT</span>
    <span class="line-white">COURSE</span>
  </h1>

  <p class="tagline">A PROVEN SUCCESS OF <em>HELPING PEOPLE IN THEIR LIVELIHOODS</em></p>

  <div class="benefits">
    <div class="benefits__label">BUSINESS SKILLS<br>THAT WILL<br>HELP YOU:</div>
    <div class="benefit benefit--job">
      <svg width="38" height="34" viewBox="0 0 38 34" aria-hidden="true">
        <rect x="2" y="7" width="30" height="22" rx="3" fill="var(--navy)"/>
        <rect x="11" y="2" width="12" height="7" rx="2" fill="none" stroke="var(--navy)" stroke-width="3"/>
        <rect x="2" y="15" width="30" height="2" fill="var(--white)"/>
        <circle cx="29" cy="26" r="7" fill="var(--navy)" stroke="var(--white)" stroke-width="1.5"/>
        <path d="M25.5 26 L28 28.5 L32.5 23.5" fill="none" stroke="var(--white)" stroke-width="2"/>
      </svg>
      <span>Get a<br>quality job</span>
    </div>
    <div class="benefit benefit--business">
      <svg width="40" height="38" viewBox="0 0 40 38" aria-hidden="true">
        <rect x="4" y="24" width="6" height="11" fill="var(--navy)"/>
        <rect x="13" y="19" width="6" height="16" fill="var(--navy)"/>
        <rect x="22" y="22" width="6" height="13" fill="var(--navy)"/>
        <rect x="31" y="13" width="6" height="22" fill="var(--navy)"/>
        <rect x="1" y="35" width="38" height="2.5" fill="var(--navy)"/>
        <polyline points="3,18 14,9 22,14 36,3" fill="none" stroke="var(--navy)" stroke-width="2.5"/>
        <polygon points="30,2 38,1 37,9" fill="var(--navy)"/>
      </svg>
      <span>start/grow<br>your business</span>
    </div>
    <div class="benefit benefit--salary">
      <svg width="40" height="40" viewBox="0 0 40 40" aria-hidden="true">
        <text x="14" y="13" font-family="Poppins, sans-serif" font-weight="700" font-size="14" fill="var(--navy)">$</text>
        <polygon points="20,16 30,26 10,26" fill="var(--navy)"/>
        <rect x="16" y="26" width="8" height="10" fill="var(--navy)"/>
        <rect x="2" y="20" width="10" height="2.5" fill="var(--navy)"/>
        <rect x="28" y="20" width="10" height="2.5" fill="var(--navy)"/>
        <rect x="2" y="28" width="10" height="2.5" fill="var(--navy)"/>
        <rect x="28" y="28" width="10" height="2.5" fill="var(--navy)"/>
        <rect x="2" y="36" width="36" height="2.5" fill="var(--navy)"/>
      </svg>
      <span>Increase<br>your salary</span>
    </div>
  </div>

  <div class="topics">
    <ul class="topics__col topics__col--a">
      <li>BUSINESS ADMIISTRATION</li>
      <li>SMALL BUSINESS MANAGEMENT</li>
      <li>FINANCE</li>
      <li>INVESTMENTS</li>
      <li>COMPUTERS</li>
      <li>ACCOUNTING</li>
      <li>SALES</li>
    </ul>
    <div class="topics__rule topics__rule--first"></div>
    <ul class="topics__col topics__col--b">
      <li>MARKETING</li>
      <li>PROJECT MANAGEMENT INTERVIEWING SKILLS</li>
      <li>BUSINESS LAW</li>
      <li>NEGOTIATION</li>
      <li>PUBLIC SPEAKING</li>
      <li>IMPORT/EXPORT</li>
      <li>INFORMATION TECHNOLOY</li>
    </ul>
    <div class="topics__rule topics__rule--second"></div>
    <ul class="topics__col topics__col--c">
      <li>DISTRIBUTION</li>
      <li>MARKETING</li>
      <li>LEDGERKEEP</li>
      <li>REAL ESTATE</li>
      <li>HEALTH CARE</li>
      <li>MANAGEMENT</li>
      <li>MARKETLY</li>
    </ul>
  </div>

</div>
</body>
</html>
```